Banner Ad Design Project

I place ads in Clickrow and also get traffic from sites like http://www.wellspringlistings.example.au/ to offer our free meditation CD and report at http://quietmindful.example.au/get-the-free-meditation-cd
We need new designs to improve this campaign.
Target Market(s)
40+ year old women, looking for personal growth or help with stress, depression, anxiety, sleep problems, health issues, memory/concentration issues
Industry/Entity Type
Campaign

```html
<!DOCTYPE html>
<html lang="en">
<head>
<meta charset="utf-8">
<title>Free Meditation CD Banner</title>
<link rel="stylesheet" href="https://fonts.googleapis.com/css2?family=Arimo:wght@400;700&family=Tinos:ital,wght@0,400;0,700;1,400&display=swap">
<style>
  :root {
    --cream-top: #fcdcb8;
    --cream-mid: #fff1df;
    --cream-low: #fdf7ee;
    --sky: #1e8ad6;
    --navy-text: #17286e;
    --price: #f08a1c;
    --panel-edge: #6bb8ec;
    --panel-mid: #1c4fa6;
    --panel-deep: #0a1b66;
    --gold: #f6c60a;
    --white: #ffffff;
  }
  html, body {
    margin: 0;
    padding: 0;
    overflow: hidden;
    background: var(--white);
  }
  .banner {
    position: relative;
    width: 1200px;
    height: 214px;
    overflow: hidden;
    font-family: "Arimo", Arial, sans-serif;
    background: linear-gradient(180deg, var(--cream-top) 0%, var(--cream-mid) 45%, var(--cream-low) 100%);
  }
  .cd-artwork {
    position: absolute;
    left: 12px;
    top: 6px;
    width: 134px;
    height: 134px;
    border-radius: 50%;
    background: radial-gradient(circle at 50% 50%, #ffffff 0 12%, #cfe4f3 13% 40%, #5fa5d8 60%, #2d6fb3 100%);
    box-shadow: 0 2px 6px rgba(20, 40, 90, 0.35);
  }
  .cd-label {
    position: absolute;
    left: 18px;
    top: 162px;
    margin: 0;
    font-size: 28px;
    line-height: 34px;
    font-weight: 700;
    color: var(--navy-text);
    letter-spacing: 0.5px;
  }
  .offer {
    position: absolute;
    left: 186px;
    top: 14px;
    width: 420px;
    text-align: center;
    margin: 0;
  }
  .offer-title {
    margin: 0;
    font-size: 30px;
    font-weight: 700;
    color: var(--sky);
    line-height: 40px;
  }
  .offer-details {
    margin: 0;
    font-size: 28px;
    font-weight: 700;
    color: var(--navy-text);
    line-height: 34px;
  }
  .offer-price {
    color: var(--price);
  }
  .brand-panel {
    position: absolute;
    left: 0;
    top: 0;
    width: 1200px;
    height: 214px;
  }
  .brand-name {
    position: absolute;
    left: 722px;
    top: 64px;
    margin: 0;
    font-family: "Tinos", "Times New Roman", serif;
    font-weight: 400;
    font-size: 60px;
    line-height: 68px;
    color: var(--gold);
    white-space: nowrap;
  }
  .brand-tagline {
    position: absolute;
    margin: 0;
    font-family: "Tinos", "Times New Roman", serif;
    font-style: italic;
    font-size: 23px;
    line-height: 28px;
    color: var(--white);
    white-space: nowrap;
  }
  .brand-tagline--lead {
    left: 728px;
    top: 142px;
  }
  .brand-tagline--close {
    right: 12px;
    top: 174px;
  }
  .brand-tagline u {
    text-underline-offset: 3px;
  }
</style>
</head>
<body>
  <main class="banner">
    <div class="cd-artwork" role="img" aria-label="Meditation CD disc artwork showing a seated meditator"></div>
    <p class="cd-label">FREE CD</p>

    <section class="offer">
      <h1 class="offer-title">FREE Meditation CD</h1>
      <p class="offer-details">and Special Report<br>"How to Find Deeper Calm<br>in Just Minutes a Day!",<br>valued at <span class="offer-price">$37</span></p>
    </section>

    <svg class="brand-panel" viewBox="0 0 1200 214" aria-hidden="true">
      <defs>
        <linearGradient id="panel-fill" x1="0" y1="0" x2="1" y2="0">
          <stop offset="0" stop-color="var(--panel-edge)"/>
          <stop offset="0.12" stop-color="var(--panel-mid)"/>
          <stop offset="0.55" stop-color="var(--panel-deep)"/>
          <stop offset="1" stop-color="var(--panel-deep)"/>
        </linearGradient>
      </defs>
      <path d="M645 0 H1200 V214 H615 C660 150 668 70 645 0 Z" fill="url(#panel-fill)"/>
    </svg>

    <h2 class="brand-name">Quiet Mindful</h2>
    <p class="brand-tagline brand-tagline--lead">All the benefits of meditation...</p>
    <p class="brand-tagline brand-tagline--close">...<u>without</u> the hard work!</p>
  </main>
</body>
</html>
```